SunMeadow Yoga Website Design

Business Logo - attached
5 pages being:
Home
About
Classes
Blog
Contact

Would like Scrolling webpage and yoga symbols to be used.

Must have's being:
Easy to navigate, Text needs to be able to be edited/updated, Enquire Now Links, More Information Links, be a secure site, SEO,

Please refer to attached document for the information for the body of the website.

Target Market(s)

Educators, Community Service, Health and Wellbeing, Mental Health

Industry/Entity Type

Yoga

Coding

Coded - Design and coding required

Number of Pages Required

5+ page

Font styles to use
Other font styles liked:
• Bella Bold BC

Colors
0094D4
00A9DD
6FCCEA
C7EBF8
E9F6FB
6B429C
8869AF
B7A5CE
E3DAEB
F3F0F8

Requirements
Must have
• Easy to navigate, Text needs to be able to be edited/updated, Enquire Now Links, More Information Links, be a secure site, SEO,
Nice to have
• Scrolling webpage, yoga symbols

```html
<!DOCTYPE html>
<html lang="en">
<head>
<meta charset="utf-8">
<title>SunMeadow Yoga</title>
<link href="https://fonts.googleapis.com/css2?family=Inter:wght@400;500;600&family=Kaushan+Script&display=swap" rel="stylesheet">
<style>
:root{
  --purple-deep:#6B429C;
  --purple:#8869AF;
  --purple-soft:#B7A5CE;
  --lilac:#E3DAEB;
  --lilac-bg:#F1E8FB;
  --lilac-blob:#DFCDF6;
  --blue-tick:#3BA3DD;
  --blue-blob:#A2DEFB;
  --text:#1d1d1f;
  --white:#ffffff;
}
*{box-sizing:border-box;margin:0;padding:0}
html,body{width:1200px;height:3227px;overflow:hidden}
body{position:relative;background:var(--white);font-family:"Inter",sans-serif;color:var(--text);font-size:13.5px;line-height:23.4px}
.abs{position:absolute}
.script{font-family:"Kaushan Script",cursive;color:var(--purple-deep);font-weight:400}

/* header */
.site-header{position:absolute;left:0;top:0;width:1200px;height:108px;background:var(--white);z-index:2}
.brand{left:48px;top:40px;display:flex;align-items:center;gap:8px;color:var(--purple);font-size:15px;font-weight:500}
.brand-dot{width:14px;height:14px;border-radius:50%;background:var(--purple-soft)}
.main-nav a{position:absolute;top:48px;color:var(--purple);text-decoration:none;font-size:13.5px}
.btn{background:var(--purple);color:var(--white);border-radius:16px;text-align:center;font-size:14px;text-decoration:none}
.login{left:1010px;top:44px;width:140px;height:28px;line-height:28px}

/* hero */
.hero-bg{left:0;top:108px}
.hero-title{left:125px;top:188px;font-size:84px;line-height:110px;white-space:nowrap}
.hero-copy{left:127px;top:292px;width:445px}
.hero-copy p{margin-bottom:23.4px}
.photo{border-radius:6px}
.hero-photo{left:586px;top:288px;width:592px;height:276px;background:linear-gradient(90deg,#c9a6e6 0%,#a9e0ef 55%,#c7cde6 100%);opacity:.85;border-radius:40px 40px 12px 12px}

/* benefits */
.benefits-title{left:0;width:1200px;top:840px;text-align:center;font-size:60px;line-height:100px}
.benefits-copy{left:128px;top:953px;width:930px}

/* lists */
.section-title{font-size:42px;line-height:60px;white-space:nowrap}
.ticks{list-style:none}
.ticks li{position:relative;padding-left:27px;height:auto}
.ticks li::before{content:"";position:absolute;left:0;top:4px;width:16px;height:16px;border-radius:50%;background:var(--blue-tick)}
.ticks li::after{content:"";position:absolute;left:5px;top:7px;width:4px;height:7px;border:solid var(--white);border-width:0 2px 2px 0;transform:rotate(45deg)}

.bodies-title{left:121px;top:1232px}
.bodies-list{left:121px;top:1312px;width:400px}
.bodies-list li{margin-bottom:13.3px}
.bodies-photo{left:640px;top:1300px;width:500px;height:210px;background:linear-gradient(90deg,#d9c6e6,#b06fe0 60%,#2cc0d8);opacity:.8;border-radius:20px}

.minds-title{left:727px;top:1700px}
.minds-list{left:715px;top:1779px;width:400px}
.minds-list li{margin-bottom:13px}
.minds-photo{left:90px;top:1690px;width:540px;height:300px;background:linear-gradient(135deg,#e9e6ef,#b67fe6 45%,#4b8de8 75%,#ececec);opacity:.75;border-radius:60px}

.spirits-title{left:112px;top:2172px}
.spirits-list{left:112px;top:2250px;width:400px}
.spirits-list li{margin-bottom:15px}
.spirits-photo{left:670px;top:2170px;width:420px;height:380px;background:linear-gradient(90deg,#eac9d8,#d6a5d9 40%,#7a96e2 70%,#3a3550);opacity:.7;border-radius:120px 120px 0 0}

/* footer */
.site-footer{left:0;top:2631px;width:1200px;height:596px;background:var(--lilac-bg)}
.foot-head{position:absolute;color:var(--purple);font-weight:600;font-size:15px}
.foot-links{position:absolute;list-style:none;font-size:13.5px;font-weight:500;line-height:27.5px}
.contact-line{position:absolute;display:flex;align-items:center;gap:8px;font-size:13.5px;font-weight:500}
.social{position:absolute;top:2881px;width:28px;height:28px;border-radius:50%}
.store-badge{position:absolute;top:2964px;height:25px;border-radius:4px;background:#111}
.form-label{position:absolute;left:839px;font-size:13.5px}
.field{position:absolute;left:839px;width:247px;background:var(--white);border:none;border-radius:5px;font-family:inherit;font-size:11.5px;padding:12px 13px;color:#888;resize:none}
.send{left:944px;top:3129px;width:142px;height:28px;line-height:28px}
</style>
</head>
<body>

<header class="site-header">
  <div class="abs brand"><span class="brand-dot"></span>SunMeadow Yoga</div>
  <nav class="main-nav">
    <a href="#" style="left:332px">Home</a>
    <a href="#" style="left:436px">About</a>
    <a href="#" style="left:540px">Classes</a>
    <a href="#" style="left:656px">Blog</a>
    <a href="#" style="left:751px">Contact</a>
  </nav>
  <a href="#" class="abs btn login">Log in</a>
</header>

<svg class="abs hero-bg" width="1200" height="680" viewBox="0 0 1200 680" aria-hidden="true">
  <path fill="var(--lilac-bg)" d="M0 0H1200V560C1100 640 900 600 780 580C620 560 480 670 300 660C160 652 60 600 0 570Z"/>
  <path fill="#E9DBFA" d="M120 0H900C820 40 680 60 640 150C600 260 560 420 420 460C300 480 180 440 130 380C80 300 150 200 120 0Z" opacity=".35"/>
  <path fill="var(--lilac-blob)" d="M626 0H910C930 80 940 150 980 240C1030 340 1120 330 1200 300V560C1130 630 1030 650 940 640C820 630 760 560 720 480C680 400 620 380 630 280C640 200 700 170 690 110C680 60 640 40 626 0Z"/>
  <path fill="#E7D8F9" d="M1010 40C1080 0 1180 30 1200 110C1210 190 1160 210 1110 190C1060 170 1000 150 1000 100C1000 70 1003 50 1010 40Z"/>
  <path fill="#EADDFB" d="M0 380C40 360 90 420 95 480C100 530 60 560 0 540Z"/>
</svg>

<h1 class="abs script hero-title">SunMeadow Yoga</h1>
<div class="abs hero-copy">
  <p>SunMeadow Yoga believe that you are never too young to benefit from and fall in love with yoga.</p>
  <p>My aim is to EMPOWER kids and teens to thrive by teaching life skills in Yoga, Mindfulness and Breathing techniques to deal with daily challenges and big emotions.</p>
  <p>SunMeadow Yoga gives kids an opportunity to enjoy and experience yoga for themselves and primarily focuses on programs for Schools, Pre Schools and Early Learning Centres, Private Classes, Sporting Clubs, Martial Arts Schools, Scout Groups and Occupational Therapy Centres just to name a few.</p>
  <p>All classes are age appropriate and encourage children’s natural drive to learn, move, and be creative.</p>
</div>
<div class="abs hero-photo" role="img" aria-label="Photo of a woman and two young girls sitting cross-legged in a meditation pose on a yoga mat"></div>

<h2 class="abs script benefits-title">Benefits of yoga</h2>
<div class="abs benefits-copy">
  <p>The benefits of yoga can last a lifetime. It is my aim &amp; passion to introduce yoga to kids of all ages and backgrounds so that they can not only experience the benefits of yoga but fall in love with the practice.<br>
  SunMeadow Yoga combines all the benefits of traditional yoga and a lot of fun!<br>
  We play games and practice engaging flows which get our bodies moving, then we take a quiet moment to be still and calm as we focus on our breathing.</p>
  <p style="margin-top:23.4px">SunMeadow Yoga Kids will learn that relaxation is just as important as moving their bodies, and the exercises which they learn in class can easily be repeated at any time in their busy day to feel calm and grounded.</p>
</div>

<!-- healthy bodies -->
<h3 class="abs script section-title bodies-title">Healthy bodies:</h3>
<ul class="abs ticks bodies-list">
  <li>Develops strong, flexible and healthy bodies</li>
  <li>Promotes spinal alignment and good posture</li>
  <li>Builds energy and stamina</li>
  <li>Improves internal physical function - organs, digestion, elimination, circulation, and blood flow.</li>
  <li>Helps breathing and lung capacity</li>
  <li>Teaches the enjoyment of movement</li>
  <li>Works the ‘whole’ body</li>
</ul>
<svg class="abs" style="left:615px;top:1196px" width="500" height="392" viewBox="0 0 500 392" aria-hidden="true">
  <path fill="var(--blue-blob)" d="M330 10C420 -20 500 60 500 170C500 290 430 390 330 390C250 390 220 330 140 320C60 310 0 280 5 210C10 130 80 110 160 120C240 130 270 30 330 10Z"/>
</svg>
<div class="abs bodies-photo" role="img" aria-label="Photo of a woman and a girl doing the splits side by side on a yoga mat"></div>

<!-- healthy minds -->
<svg class="abs" style="left:81px;top:1666px" width="560" height="372" viewBox="0 0 560 372" aria-hidden="true">
  <path fill="var(--blue-blob)" d="M40 40C90 10 160 30 190 80C220 140 160 200 110 210C50 220 0 180 8 120C12 80 20 55 40 40Z"/>
  <path fill="var(--lilac-blob)" d="M200 20C280 -10 380 10 430 70C480 140 460 230 400 260C340 290 300 300 260 340C220 380 150 380 140 320C130 260 170 230 180 170C190 110 140 50 200 20Z"/>
</svg>
<div class="abs minds-photo" role="img" aria-label="Photo of three girls in backbend bridge poses, viewed from above"></div>
<h3 class="abs script section-title minds-title">Healthy minds:</h3>
<ul class="abs ticks minds-list">
  <li>Cultivates confidence and self-esteem</li>
  <li>Develops concentration and attention</li>
  <li>Clears the mind for better clarity and decision making</li>
  <li>Helps relax and sleep better</li>
  <li>Calms the nervous system</li>
  <li>Learns to cope with stressful situations</li>
  <li>Balances emotions</li>
</ul>

<!-- healthy spirits -->
<h3 class="abs script section-title spirits-title">Healthy spirits:</h3>
<ul class="abs ticks spirits-list">
  <li>Fosters creativity, expression and imagination</li>
  <li>Cultivates kindness to themselves and others</li>
  <li>Cultivates respect for self and others</li>
  <li>Teaches self-awareness</li>
  <li>Builds balance and inner quiet</li>
  <li>Builds inner strength and resilienc</li>
  <li>Focuses on positive self-talk</li>
</ul>
<svg class="abs" style="left:626px;top:2136px" width="506" height="415" viewBox="0 0 506 415" aria-hidden="true">
  <path fill="var(--lilac-blob)" d="M120 10C200 -10 260 40 290 60C330 90 380 40 440 70C500 100 480 180 450 200C420 230 500 260 500 330C500 390 440 413 380 413H80C20 400 0 340 5 270C10 200 60 160 50 110C40 60 70 20 120 10Z"/>
</svg>
<div class="abs spirits-photo" role="img" aria-label="Photo of two young girls sitting back to back with palms pressed together"></div>

<!-- footer -->
<footer class="abs site-footer"></footer>
<div class="foot-head" style="left:114px;top:2697px">Lumora</div>
<ul class="foot-links" style="left:114px;top:2734px"><li>Home</li><li>Advertise</li><li>Register</li></ul>
<div class="foot-head" style="left:296px;top:2697px">Rules</div>
<ul class="foot-links" style="left:296px;top:2734px"><li>FAQs</li><li>Terms and Conditions</li><li>Privacy Policy</li></ul>

<div class="foot-head" style="left:534px;top:2697px">Contact Us</div>
<div class="contact-line" style="left:534px;top:2740px">
  <svg width="18" height="14" viewBox="0 0 18 14" aria-hidden="true"><rect x="1" y="1" width="16" height="12" rx="2" fill="none" stroke="var(--purple)" stroke-width="1.5"/><path d="M1.5 2L9 8L16.5 2" fill="none" stroke="var(--purple)" stroke-width="1.5"/></svg>
  hello@sunmeadowyoga.com</div>
<div class="contact-line" style="left:534px;top:2772px">
  <svg width="18" height="18" viewBox="0 0 24 24" aria-hidden="true"><path d="M5 3h4l2 5-2.5 1.5a11 11 0 0 0 6 6L16 13l5 2v4a2 2 0 0 1-2 2A17 17 0 0 1 3 5a2 2 0 0 1 2-2z" fill="none" stroke="var(--purple)" stroke-width="1.6"/></svg>
  + 91 0987654321</div>
<div class="contact-line" style="left:534px;top:2805px">
  <svg width="18" height="18" viewBox="0 0 24 24" aria-hidden="true"><path d="M12 22s7-7 7-12a7 7 0 0 0-14 0c0 5 7 12 7 12z" fill="none" stroke="var(--purple)" stroke-width="1.6"/><circle cx="12" cy="10" r="2.5" fill="none" stroke="var(--purple)" stroke-width="1.6"/></svg>
  48, Lotus Lane, Meadowvale</div>
<div class="foot-head" style="left:534px;top:2842px">Social Media</div>
<span class="social" style="left:533px;background:#1877F2"></span>
<span class="social" style="left:572px;background:#D6249F"></span>
<span class="social" style="left:610px;background:#1DA1F2"></span>
<span class="social" style="left:649px;background:#25D366"></span>
<div class="foot-head" style="left:534px;top:2925px">Download The App</div>
<span class="store-badge" style="left:540px;width:85px"></span>
<span class="store-badge" style="left:633px;width:86px"></span>

<div class="foot-head" style="left:839px;top:2697px">Or Connect With Us Here!</div>
<label class="form-label" style="top:2736px">Your Email</label>
<input class="field" style="top:2771px;height:47px" placeholder="Enter Your Email">
<label class="form-label" style="top:2835px">Your Phone Number</label>
<input class="field" style="top:2870px;height:46px" placeholder="Enter Your Phone Number">
<label class="form-label" style="top:2934px">Your Issue</label>
<textarea class="field" style="top:2969px;height:129px" placeholder="Briefly describe your issue"></textarea>
<a href="#" class="abs btn send">Send</a>

</body>
</html>
```